Website Design for my CNC machine Shop.

I need a new website for my Machining Company.

It can be a simple website that acts more like an "Online Business card" I has to highlight the services I provide and give Companies the confidence to engage my services.

I needs it to be a really modern or even a little futuristic promoting my Company.

I have just moved locations and have renovated the premises and would be great to let everyone know along with a new website.

If you can help with linking it to search engines to help get more exposure that would be great.

It needs to accommodate the three main services I provide which will include capacities of each machine (within that service) and maybe a couple images.
CNC Machining (5-axis, 3-axis)
EDM Wire cutting
3D Metal Printing
Along with home page and Contact page

I have two websites and you can use the txt from either/combination of these.
www.korvaltooling.com.au
(no longer do Laser Marking and etching but now do 3D metal Printing)
www.tarnquill.com.au

Happy to chat further with the designer

Company logo's provided.

For Images: I am happy to use Glimmerbay and can purchase any images you like
EDM Wire cut
https://www.glimmerbay-pics.com/search/edm-wire-cutting

CNC Machining:
https://www.glimmerbay-pics.com/search/vertical-cnc-machining
Don't use any with engines or motor vehicle parts

3D metal Printing
https://www.glimmerbay-pics.com/search/slm-metal-printing

Target Market(s)

Defence, Aerospace, Medical, HIgh Precision

Industry/Entity Type

Mechanical Engineering

Coding

Coded - Design and coding required

Number of Pages Required

5+ page

Requirements
Must have
• Home page, 3 services, Contacts. Can add image to each of the services

```html
<!DOCTYPE html>
<html lang="en">
<head>
<meta charset="utf-8">
<title>Veskar Precision Machinists</title>
<link rel="stylesheet" href="https://fonts.googleapis.com/css2?family=Poppins:wght@300;400;500;600;700&display=swap">
<style>
:root{
  --green:#3bb482;
  --green-dark:#2f9e70;
  --navy:#10293a;
  --navy-deep:#0c2433;
  --ink:#1d2b36;
  --text:#3a4550;
  --hatch:#e4e4e4;
  --white:#ffffff;
}
*{margin:0;padding:0;box-sizing:border-box}
html,body{width:1200px;height:5137px;overflow:hidden}
body{position:relative;font-family:'Poppins',sans-serif;color:var(--text);background:var(--white)}
.abs{position:absolute}
.topbar{left:0;top:0;width:1200px;height:46px;background:var(--green);color:#fff;font-size:16px}
.topbar .item{position:absolute;top:9px;display:flex;align-items:center;gap:8px}
.topbar .dot{width:30px;height:30px;border-radius:50%;background:#fff;display:flex;align-items:center;justify-content:center}
.header{left:0;top:46px;width:1200px;height:94px;background:#fff}
.brand{position:absolute;left:72px;top:10px}
.brand .name{font-size:54px;font-weight:600;letter-spacing:3px;color:#5d7380;line-height:56px}
.brand .tag{font-size:11px;letter-spacing:3.2px;color:var(--green);margin-top:2px}
.nav{position:absolute;top:38px;left:0;font-size:12px;color:var(--ink)}
.nav a{position:absolute;white-space:nowrap;text-decoration:none;color:inherit}
.nav a.active{color:var(--green)}
.nav a.active::after{content:"";position:absolute;left:0;right:0;top:22px;height:4px;background:#a9b3b8}
.hero{left:0;top:140px;width:1200px;height:734px;background:linear-gradient(120deg,#2c2c2c 0%,#4a4a4a 35%,#1b1b1b 70%,#0f0f0f 100%)}
.hero-title{left:0;top:370px;width:1200px;text-align:center;color:#fff;font-size:50px;font-weight:600;line-height:64px}
.hero-sub{left:0;top:436px;width:1200px;text-align:center;color:var(--green);font-size:29px;font-weight:400}
.hero-copy{left:0;top:520px;width:1200px;text-align:center;color:#fff;font-size:17px;line-height:28px}
.btn{position:absolute;display:flex;align-items:center;justify-content:center;font-size:17px;color:#fff;background:var(--green);border:2px solid var(--green);outline:3px solid var(--green);outline-offset:-7px;box-shadow:inset 0 0 0 4px #fff0}
.btn.framed{border:3px solid var(--green);box-shadow:inset 0 0 0 2px #fff}
.btn.navy{background:var(--navy);border:3px solid var(--navy);box-shadow:inset 0 0 0 2px #fff;outline:none}
.section-title{left:0;width:1200px;text-align:center;color:var(--ink);font-size:52px;font-weight:500}
.section-sub{left:0;width:1200px;display:flex;justify-content:center;align-items:center;gap:14px;color:var(--green);font-size:26px}
.dbl{width:78px;height:8px;border-top:2px solid #7a8790;border-bottom:2px solid #7a8790}
.hatch{background:var(--hatch)}
.photo{background:linear-gradient(135deg,#9a9a9a,#3e3e3e)}
.svc-title{font-size:40px;color:var(--ink);font-weight:500}
.rule{height:3px;width:57px;background:var(--green)}
.svc-copy{font-size:13.5px;line-height:22px;color:var(--text);width:480px}
.svc-copy p+p{margin-top:24px}
.about-photo{left:480px;top:3453px;width:720px;height:592px;background:linear-gradient(120deg,#3a3a3a,#8a8a8a 45%,#2a2a2a)}
.card{position:absolute;top:4336px;width:328px;height:226px;background:#fff;box-shadow:0 2px 14px rgba(0,0,0,.12)}
.card::after{content:"";position:absolute;left:0;right:0;bottom:0;height:6px;background:linear-gradient(90deg,var(--navy) 50%,var(--green) 50%)}
.card .avatar{position:absolute;left:18px;top:30px;width:66px;height:66px;border-radius:50%;background:#c9cdd0}
.card .who{position:absolute;left:105px;top:44px;font-size:15px;font-weight:600;color:var(--navy)}
.card .role{position:absolute;left:105px;top:66px;font-size:11px;color:var(--green)}
.card .quote{position:absolute;right:22px;top:86px}
.card .said{position:absolute;left:26px;top:124px;width:280px;font-size:13px;line-height:22px}
.footer{left:0;top:4737px;width:1200px;height:323px;background:var(--navy-deep);color:#fff}
.footer h4{position:absolute;top:72px;font-size:16px;font-weight:500}
.footer h4::after{content:"";position:absolute;left:0;top:32px;width:26px;height:2px;background:var(--green)}
.links{position:absolute;left:390px;top:127px;font-size:12.5px;line-height:27px;list-style:none}
.links li::before{content:"›";color:var(--green);margin-right:8px}
.contact-row{position:absolute;left:662px;display:flex;gap:14px;font-size:12.5px;line-height:15px}
.contact-row .ic{width:28px;height:28px;border:1px solid #5b7080;display:flex;align-items:center;justify-content:center}
.social{position:absolute;top:253px;width:30px;height:30px;border:2px solid #fff}
.copyright{left:0;top:5060px;width:1200px;height:77px;background:var(--green);color:#fff;font-size:11px;text-align:center;line-height:44px}
</style>
</head>
<body>

<div class="abs topbar">
  <div class="item" style="left:733px"><span class="dot"><svg width="16" height="16" viewBox="0 0 24 24"><path d="M6.6 10.8a15 15 0 0 0 6.6 6.6l2.2-2.2a1 1 0 0 1 1-.25 11 11 0 0 0 3.6.6 1 1 0 0 1 1 1V20a1 1 0 0 1-1 1A17 17 0 0 1 3 4a1 1 0 0 1 1-1h3.5a1 1 0 0 1 1 1 11 11 0 0 0 .6 3.6 1 1 0 0 1-.25 1z" fill="#3bb482"/></svg></span>xxxx xxx xxx</div>
  <div class="item" style="left:896px"><span class="dot"><svg width="16" height="16" viewBox="0 0 24 24"><rect x="3" y="6" width="18" height="12" rx="1" fill="#3bb482"/><path d="M3 6l9 7 9-7" stroke="#fff" stroke-width="1.5" fill="none"/></svg></span>info@veskarmachinists.com</div>
</div>

<div class="abs header">
  <div class="brand"><div class="name">VESKAR</div><div class="tag">PRECISION MACHINISTS</div></div>
  <nav class="nav">
    <a class="active" style="left:450px">HOME</a>
    <a style="left:518px">ABOUT US</a>
    <a style="left:612px">EDM WIRE CUTTING</a>
    <a style="left:764px">CNC MACHINING</a>
    <a style="left:904px">3D METAL PRINTING</a>
    <a style="left:1058px">CONTACT</a>
  </nav>
</div>

<div class="abs hero" role="img" aria-label="Dark close-up of a CNC milling spindle and cutting tool"></div>
<h1 class="abs hero-title">WE ARE AN INNOVATIVE&nbsp; COMPANY</h1>
<div class="abs hero-sub">THAT SPECIALISE IN TECHNICAL AND CREATIVE ENGINEERING</div>
<p class="abs hero-copy">Our core sectors of expertise are in EDM wire cutting, 3DMetal Printing and CNC machining.<br>With our combination of highly skilled staff and sophisticated machinery we offer a<br>comprehensive and professional service</p>
<div class="btn framed" style="left:497px;top:650px;width:207px;height:54px">CONTACT US</div>

<h2 class="abs section-title" style="top:995px">OUR SERVICES</h2>
<div class="abs section-sub" style="top:1071px"><span class="dbl"></span>WHAT WE DO<span class="dbl"></span></div>

<!-- EDM -->
<div class="abs hatch" style="left:74px;top:1527px;width:251px;height:270px"></div>
<div class="abs photo" style="left:107px;top:1211px;width:562px;height:163px;background:linear-gradient(90deg,#8a8a8a,#3d3d3d)" role="img" aria-label="Hand placing a part in an EDM wire cutting machine"></div>
<div class="abs photo" style="left:107px;top:1374px;width:421px;height:391px;background:linear-gradient(160deg,#6f6f6f,#b8a58a 55%,#4a4a4a)"></div>
<h3 class="abs svc-title" style="left:603px;top:1397px">EDM WIRE CUT</h3>
<div class="abs rule" style="left:603px;top:1458px"></div>
<div class="abs svc-copy" style="left:605px;top:1504px"><p>We operate Swiss manufactured Dravelle EDM Machines which are regarded as the Ardmore Grand of wire cut machines.</p><p>There is no limit to the hardness of material: as long as it is conductive we can cut it. Wire cut machines are extremely accurate and leave and incredibly smooth surface which is not possible with other cutting methods.</p></div>
<div class="btn framed" style="left:603px;top:1699px;width:205px;height:54px">KNOW MORE</div>

<!-- CNC -->
<div class="abs hatch" style="left:883px;top:1885px;width:251px;height:270px"></div>
<div class="abs photo" style="left:541px;top:1923px;width:562px;height:134px;background:linear-gradient(90deg,#9fb3c2,#5e6e7a)" role="img" aria-label="Vertical CNC machining spindle cutting an aluminium block"></div>
<div class="abs photo" style="left:683px;top:2057px;width:420px;height:420px;background:linear-gradient(170deg,#5f6e78,#b7c2ca 55%,#2e3840)"></div>
<h3 class="abs svc-title" style="left:113px;top:2105px">CNC MACHINING</h3>
<div class="abs rule" style="left:113px;top:2166px"></div>
<div class="abs svc-copy" style="left:117px;top:2214px"><p>With our combination of high quality Torvane Machining Centres we are able to provide innovative solutions to your precision CNC machining requirements.</p><p>Varying from general 2-D projects to more complex 3-D machining of prototypes and assemblies we are able to satisfy most medium size engineering requirements.</p></div>
<div class="btn framed" style="left:115px;top:2411px;width:205px;height:54px">KNOW MORE</div>

<!-- 3D -->
<div class="abs hatch" style="left:66px;top:2625px;width:251px;height:268px"></div>
<div class="abs photo" style="left:107px;top:2667px;width:562px;height:163px;background:linear-gradient(90deg,#7e9cb9,#c7d6e3)" role="img" aria-label="Precision printed metal fittings in blue light"></div>
<div class="abs photo" style="left:107px;top:2830px;width:421px;height:391px;background:linear-gradient(160deg,#6d8eae,#c2d1de 50%,#4b6985)"></div>
<h3 class="abs svc-title" style="left:601px;top:2849px">3D METAL PRINTING</h3>
<div class="abs rule" style="left:603px;top:2910px"></div>
<div class="abs svc-copy" style="left:605px;top:2959px"><p>Lorem ipsum dolor sit amet, consectetur adipiscing elit, sed do eiusmod tempor incididunt ut labore et dolore magna aliqua. Quis ipsum suspen disse ultrices gravida. Risus commodo viverra maecenas accu msan lacus vel facilisis.</p><p>Lorem ipsum dolor sit amet, consectetur adipiscing elit, sed do eiusmod tempor incididunt ut labore et dolore magna aliqua.</p></div>
<div class="btn framed" style="left:603px;top:3157px;width:205px;height:54px">KNOW MORE</div>

<!-- About -->
<div class="abs about-photo" role="img" aria-label="Lathe tool turning metal with flying chips"></div>
<svg class="abs" style="left:0;top:3453px" width="620" height="592"><polygon points="0,0 484,0 616,296 484,592 0,592" fill="#3bb482"/></svg>
<h2 class="abs" style="left:75px;top:3555px;font-size:52px;font-weight:500;color:#fff">ABOUT US</h2>
<div class="abs" style="left:75px;top:3614px;font-size:21px;color:#fff">VESKAR PRECISION MACHINIST</div>
<div class="abs" style="left:75px;top:3659px;width:80px;height:8px;border-top:2px solid #fff;border-bottom:2px solid #fff"></div>
<p class="abs" style="left:76px;top:3720px;width:440px;font-size:13.5px;line-height:22px;color:#fff">Lorem ipsum dolor sit amet, consectetur adipiscing elit, sed do eiusmod tempor incididunt ut labore et dolore magna aliqua. Quis ipsum suspendisse ultrices gravida. Risus commodo viverra maecenas accumsan lacus vel facilisis.</p>
<div class="btn navy" style="left:76px;top:3884px;width:206px;height:54px">CONTACT US</div>

<!-- Testimonials -->
<h2 class="abs section-title" style="top:4195px">TESTIMONIALS</h2>
<div class="abs section-sub" style="top:4265px"><span class="dbl"></span>CLIENT REVIEWS<span class="dbl"></span></div>

<div class="card" style="left:92px"><div class="avatar" role="img" aria-label="Client portrait"></div><div class="who">Daniel Reeves</div><div class="role">Client</div><svg class="quote" width="44" height="28"><rect x="0" y="8" width="18" height="20" fill="#e0e0e0"/><rect x="24" y="8" width="18" height="20" fill="#e0e0e0"/></svg><p class="said">Lorem ipsum dolor sit amet, consect etur adipiscing elit, sed do eiusmod tempor incididunt ut labore et</p></div>
<div class="card" style="left:449px"><div class="avatar" role="img" aria-label="Client portrait"></div><div class="who">Daniel Reeves</div><div class="role">Client</div><svg class="quote" width="44" height="28"><rect x="0" y="8" width="18" height="20" fill="#e0e0e0"/><rect x="24" y="8" width="18" height="20" fill="#e0e0e0"/></svg><p class="said">Lorem ipsum dolor sit amet, consect etur adipiscing elit, sed do eiusmod tempor incididunt ut labore et</p></div>
<div class="card" style="left:806px"><div class="avatar" role="img" aria-label="Client portrait"></div><div class="who">Daniel Reeves</div><div class="role">Client</div><svg class="quote" width="44" height="28"><rect x="0" y="8" width="18" height="20" fill="#e0e0e0"/><rect x="24" y="8" width="18" height="20" fill="#e0e0e0"/></svg><p class="said">Lorem ipsum dolor sit amet, consect etur adipiscing elit, sed do eiusmod tempor incididunt ut labore et</p></div>

<svg class="abs" style="left:562px;top:4638px" width="76" height="12"><circle cx="6" cy="6" r="4.5" fill="#3bb482"/><circle cx="30" cy="6" r="3.5" fill="#cfd8dd"/><circle cx="48" cy="6" r="3.5" fill="#cfd8dd"/><circle cx="66" cy="6" r="3.5" fill="#cfd8dd"/></svg>

<!-- Footer -->
<footer class="abs footer">
  <div class="brand" style="left:72px;top:108px"><div class="name" style="color:#b9c5cc">VESKAR</div><div class="tag">PRECISION MACHINISTS</div></div>
  <span class="social" style="left:113px"></span><span class="social" style="left:153px"></span><span class="social" style="left:193px"></span><span class="social" style="left:233px"></span>
  <h4 style="left:380px">QUICK LINKS</h4>
  <ul class="links"><li>ABOUT US</li><li>EDM WIRE CUTTING</li><li>CNC MACHINING</li><li>LASER MARKING AND ETCHING</li><li>CONTACT US</li></ul>
  <h4 style="left:662px">CONTACT US</h4>
  <div class="contact-row" style="top:135px"><span class="ic"><svg width="12" height="12" viewBox="0 0 24 24"><path d="M6.6 10.8a15 15 0 0 0 6.6 6.6l2.2-2.2a1 1 0 0 1 1-.25 11 11 0 0 0 3.6.6 1 1 0 0 1 1 1V20a1 1 0 0 1-1 1A17 17 0 0 1 3 4a1 1 0 0 1 1-1h3.5a1 1 0 0 1 1 1 11 11 0 0 0 .6 3.6 1 1 0 0 1-.25 1z" fill="#3bb482"/></svg></span><span>CALL US<br>0398 214 557</span></div>
  <div class="contact-row" style="top:188px"><span class="ic"><svg width="12" height="12" viewBox="0 0 24 24"><rect x="3" y="6" width="18" height="12" fill="#3bb482"/></svg></span><span>EMAIL US<br>hello@veskarmachinists.com</span></div>
  <div class="contact-row" style="top:240px"><span class="ic"><svg width="12" height="14" viewBox="0 0 24 28"><path d="M12 2a8 8 0 0 1 8 8c0 6-8 16-8 16S4 16 4 10a8 8 0 0 1 8-8z" fill="#3bb482"/><circle cx="12" cy="10" r="3" fill="#0c2433"/></svg></span><span>Address line Dummy Here<br>Address line Here</span></div>
  <h4 style="left:931px">OUR NEWSLETTER</h4>
  <p class="abs" style="left:931px;top:126px;width:220px;font-size:12.5px;line-height:17px">Subscribe our newsletter to get the latest news.</p>
  <div class="abs" style="left:931px;top:170px;width:210px;height:38px;border:1px solid #9fb0bb;font-size:11px;color:#9fb0bb;padding:10px 8px">Enter Email Address</div>
  <svg class="abs" style="left:1112px;top:180px" width="20" height="20"><circle cx="10" cy="10" r="8" stroke="#3bb482" stroke-width="1.5" fill="none"/><path d="M6 10h8M11 7l3 3-3 3" stroke="#3bb482" stroke-width="1.5" fill="none"/></svg>
</footer>
<div class="abs copyright">Copyright © 2024 All Rights Reserved By Company name</div>

</body>
</html>
```